Cork Lantern website design elements

Company: Cork Lantern
Business: Wine website (selling wine online)
www.corklantern.com.au
Please note that this is an initial project, ongoing design work will be required after this project.
Design requirement
Note: Full website design not required, only specific elements to enhance current design.
- Must work with existing logo and wood background (do not change site background)
- Must work with a orange (please improve current orange colour) and blue colour (blue colour in attachments)
- Pictures of wine bottles or wine glasses are not to be used in design elements.
I currently have an existing design which I would like certain elements designed for. Design elements must work with responsive functionality.
I am trying to achieve a modern retro feel of the website, please refer to the below websites as examples that I am trying to look like.
- https://au.pennytrimguild.com/
- http://www.harveykettle.com/italian/australia/home
- http://www.marigoldfizz.co.uk/
- http://www.netgather.org.nz/13/
As mentioned the site is already built and I need certain elements to work with what is already there. All elements must work with current logo and wood panel background.
I require the following elements
• Menu bar (must be the orange)
• Home page promo slider (Text, this weeks special etc)
• 2x homepage promo tabs buttons (Join the lantern club, what's in the box deal)
• 4x Homepage navigation tabs (Red wine, White wine, Sparkling, Pre mixed cases)
• Add to cart button
• Product image backdrop (can be wider than current examples)
o I would like the backdrops to be a different colour scheme to each other e.g red wine will habe red colour, white will have a cream colour, etc)
o I would prefer a close up of the product, does not need to be full view
Please refer to attachments for elements that I like and would like to mimic.
Colour scheme
- Use existing orange (please suggest if you think of a better tone)
- Secondary colour light baby blue (suggest best options)
- Please advise of other colours needed
Design elements to be provided in jog and raw design format.
This project will require ongoing work.
I will provide access details to site upon request.
Please contact me if you have any questions.
Rowan
Cork Lantern

```html
<!DOCTYPE html>
<html lang="en">
<head>
<meta charset="utf-8">
<title>Cork Lantern</title>
<link rel="stylesheet" href="https://fonts.googleapis.com/css2?family=Cinzel:wght@400;700&family=Ubuntu:wght@400;500&family=Tinos&display=swap">
<style>
:root{
  --wood-light:#e2c396;
  --wood-mid:#d7b584;
  --wood-dark:#cfa977;
  --panel:#ffffff;
  --orange:#ef8d45;
  --orange-soft:#f49b55;
  --orange-deep:#c9632f;
  --orange-deep-inner:#d87545;
  --tan:#d3a875;
  --tan-inner:#c39a66;
  --red:#b81015;
  --grey-card:#dcdcdc;
  --sand-card:#d5a873;
  --contact:#e3c192;
  --footer:#d86f3f;
  --ink:#2d2a26;
  --ink-soft:#5a5046;
  --gold:#f6c51a;
  --wine-red:#b5121b;
}
*{box-sizing:border-box;margin:0;padding:0}
html,body{width:1124px;height:1200px;overflow:hidden}
body{
  background:linear-gradient(90deg,var(--wood-mid) 0%,var(--wood-light) 18%,var(--wood-dark) 37%,var(--wood-light) 55%,var(--wood-mid) 74%,var(--wood-light) 100%);
  font-family:"Ubuntu",sans-serif;color:var(--ink);
}
.page{position:relative;width:1200px;height:1281px;transform:scale(.93667);transform-origin:0 0}
.abs{position:absolute}

/* header */
.brand{left:113px;top:30px;display:flex;align-items:center;gap:10px}
.brand-dot{width:22px;height:22px;border-radius:50%;background:#fff}
.brand-name{font-family:"Cinzel",serif;font-weight:700;font-size:30px;color:#fff;line-height:1}
.search{left:852px;top:34px;width:223px;height:28px;border:1px solid #c75a48;border-radius:4px;background:#fff;overflow:hidden;display:flex}
.search svg{margin:6px 8px 0 14px}
.search-input{flex:1;font-size:12px;color:#888;line-height:28px}
.search-go{width:41px;background:var(--orange-deep-inner);color:#fff;font-size:12px;text-align:center;line-height:28px}
.cart{left:950px;top:78px}
.cart-label{right:125px;top:84px;font-size:14px;text-align:right;line-height:19px;color:var(--ink)}
.cart-label small{font-size:12px;display:block}

/* main panel */
.panel{left:113px;top:138px;width:962px;height:1060px;background:var(--panel);border-radius:6px}
.nav{left:124px;top:151px;width:939px;height:49px;background:var(--orange);border-radius:3px;display:flex}
.nav a{font-family:"Cinzel",serif;font-size:19px;color:#fff;text-decoration:none;display:flex;align-items:center;justify-content:center;border-right:1px solid #d9742f}
.nav a:last-child{border:none}

/* slider */
.slider{left:124px;top:213px;width:642px;height:367px;border:1px solid #eee;border-radius:4px;background:#fff}
.slider-shadow{left:170px;top:578px;width:560px;height:22px;background:radial-gradient(ellipse at 50% 0,rgba(0,0,0,.25),rgba(0,0,0,0) 70%)}
.slide-photo{left:139px;top:230px;width:614px;height:337px;background:radial-gradient(ellipse at 55% 60%,#c9783b 0%,#8a3d17 45%,#3b1209 80%,#250806 100%)}
.slide-arrow{top:363px;width:38px;height:38px;background:rgba(0,0,0,.25);border:1px solid rgba(255,255,255,.25)}
.slide-arrow svg{display:block;margin:12px auto}
.slide-title{right:460px;top:420px;font-size:21px;color:#fff;text-align:right}
.slide-rule{left:457px;top:445px;width:283px;height:1px;background:#fff}
.slide-text{left:452px;top:450px;width:288px;font-size:13px;line-height:18px;color:#fff;text-align:right}
.shop-now{left:635px;top:519px;width:105px;height:32px;background:#1d1a18;border-radius:4px;color:#fff;font-size:15px;font-weight:500;text-align:center;line-height:32px}

/* promo tabs */
.promo{left:790px;width:273px;height:110px;border-radius:3px}
.promo-inner{position:absolute;left:10px;top:11px;width:253px;height:89px;border-radius:2px}
.promo-art{position:absolute;left:18px;top:12px;width:44px;height:66px;border-radius:4px}
.promo-label{position:absolute;left:90px;top:23px;font-family:"Cinzel",serif;font-size:19px;line-height:24px;color:#fff}

/* products */
.card{top:623px;width:288px;height:206px;border-radius:3px}
.card-shadow{top:826px;width:220px;height:14px;background:radial-gradient(ellipse at 50% 0,rgba(0,0,0,.3),rgba(0,0,0,0) 70%)}
.card-title{position:absolute;left:18px;top:20px;font-family:"Cinzel",serif;font-size:22px}
.card-price{position:absolute;left:18px;top:55px;font-family:"Cinzel",serif;font-size:17px;white-space:nowrap}
.card-price s{font-size:14px;text-decoration:none}
.card-price b{font-weight:400;font-size:20px;margin-left:6px}
.card-desc{position:absolute;left:18px;top:85px;width:180px;font-size:12px;line-height:18px}
.card-art{position:absolute;right:22px;top:18px;width:66px;height:152px;border-radius:30px 30px 8px 8px}
.add-cart{position:absolute;left:25px;top:153px;width:159px;height:36px;border-radius:4px;background:linear-gradient(#fff,#e4e4e4);box-shadow:0 1px 2px rgba(0,0,0,.25);font-size:16px;color:#222;text-align:center;line-height:36px}
.card--red{left:126px;background:var(--red);color:#fff}
.card--red .card-price b{color:var(--gold)}
.card--white{left:451px;background:var(--grey-card);color:var(--ink-soft)}
.card--white .card-title{color:var(--wine-red)}
.card--white .card-price{color:var(--ink)}
.card--sparkling{left:776px;background:var(--sand-card);color:#fff}
.card--sparkling .card-price b{color:var(--wine-red)}

/* contact */
.contact{left:126px;top:871px;width:936px;height:162px;background:var(--contact);border-radius:3px}
.contact h2{position:absolute;left:16px;top:14px;font-size:20px;font-weight:500;color:var(--ink)}
.contact-rule{position:absolute;left:16px;top:45px;width:208px;height:1px;background:#f4dfbf}
.contact-item{position:absolute;top:72px;display:flex;align-items:flex-start;gap:14px;font-size:14px;line-height:18px;color:var(--ink)}

/* footer */
.footer{left:113px;top:1065px;width:962px;height:133px;background:var(--footer);border-radius:0 0 6px 6px}
.follow{position:absolute;left:127px;top:46px;font-family:"Tinos",serif;font-size:25px;color:#fff}
.social{position:absolute;top:34px;width:70px;height:69px;display:flex;align-items:center;justify-content:center;color:#fff;font-size:12px;font-weight:500}
.copyright{left:0;width:1166px;top:1225px;text-align:center;font-size:13px;color:var(--ink);letter-spacing:.3px}
</style>
</head>
<body>
<div class="page">

  <div class="abs brand"><span class="brand-dot"></span><span class="brand-name">Cork Lantern</span></div>

  <div class="abs search">
    <svg width="18" height="18" viewBox="0 0 18 18"><circle cx="7" cy="7" r="5" fill="none" stroke="#9a9a9a" stroke-width="2"/><path d="M11 11l5 5" stroke="#9a9a9a" stroke-width="2.5"/></svg>
    <span class="search-input">Search</span>
    <span class="search-go">GO</span>
  </div>

  <svg class="abs cart" width="34" height="34" viewBox="0 0 34 34"><path d="M2 4h6l4 18h16l3-12H10" fill="none" stroke="#555" stroke-width="2"/><path d="M11 14h19M12 18h17" stroke="#888" stroke-width="1.5"/><circle cx="14" cy="28" r="2.5" fill="#555"/><circle cx="26" cy="28" r="2.5" fill="#555"/></svg>
  <div class="abs cart-label" style="right:auto;left:990px;width:86px">Shopping Cart<small>0 Items</small></div>

  <div class="abs panel"></div>

  <nav class="abs nav">
    <a style="width:202px">RED WINE</a>
    <a style="width:231px">WHITE WINE</a>
    <a style="width:211px">SPARKLING</a>
    <a style="width:295px">PRE MIXED CASES</a>
  </nav>

  <div class="abs slider"></div>
  <div class="abs slider-shadow"></div>
  <div class="abs slide-photo" role="img" aria-label="Photo of oak wine barrels in a candlelit cellar"></div>
  <div class="abs slide-arrow" style="left:140px"><svg width="10" height="14" viewBox="0 0 10 14"><path d="M8 1L2 7l6 6" fill="none" stroke="#fff" stroke-width="2"/></svg></div>
  <div class="abs slide-arrow" style="left:715px"><svg width="10" height="14" viewBox="0 0 10 14"><path d="M2 1l6 6-6 6" fill="none" stroke="#fff" stroke-width="2"/></svg></div>
  <div class="abs slide-title" style="right:auto;left:457px;width:283px">THIS WEEK SPECIAL</div>
  <div class="abs slide-rule"></div>
  <p class="abs slide-text">Class aptent taciti sociosqu ad litora torquent per conubia nostra, per inceptos himenaeos. Suspen-disse mattis tellus sit amet justo convallis, vitae</p>
  <div class="abs shop-now">SHOP NOW</div>

  <div class="abs promo" style="top:212px;background:var(--tan)">
    <div class="promo-inner" style="background:var(--tan-inner)">
      <div class="promo-art" role="img" aria-label="Wine glass illustration" style="background:linear-gradient(#3a1a12,#1c1c1c)"></div>
      <div class="promo-label">JOIN THE LANTERN<br>CLUB</div>
    </div>
  </div>
  <div class="abs promo" style="top:340px;background:var(--orange)">
    <div class="promo-inner" style="background:var(--orange-soft)">
      <div class="promo-art" role="img" aria-label="Wooden barrel illustration" style="left:14px;width:64px;top:20px;height:50px;background:linear-gradient(#c9a27a,#8a6644)"></div>
      <div class="promo-label" style="left:91px">WHAT'S IN THE<br>BOX DEAL</div>
    </div>
  </div>
  <div class="abs promo" style="top:467px;background:var(--orange-deep)">
    <div class="promo-inner" style="background:var(--orange-deep-inner)">
      <div class="promo-art" role="img" aria-label="Customer service agent illustration" style="left:20px;width:50px;background:linear-gradient(#b26a3e,#f3ece4)"></div>
      <div class="promo-label">CUSTOMER<br>SERVICE</div>
    </div>
  </div>

  <div class="abs card card--red">
    <div class="card-title">RED WINE</div>
    <div class="card-price">PRICE : <s>$00.00</s><b>$50.00</b></div>
    <p class="card-desc">Class aptent taciti sociosqu ad litora torquent per conubia nostra, per inceptos himenaeos.</p>
    <div class="card-art" role="img" aria-label="Glass of red wine" style="background:linear-gradient(#9a1b2a,#c9c9c9)"></div>
    <div class="add-cart">ADD TO CART</div>
  </div>
  <div class="abs card-shadow" style="left:160px"></div>

  <div class="abs card card--white">
    <div class="card-title">WHITE WINE</div>
    <div class="card-price">PRICE : <s>$00.00</s><b>$50.00</b></div>
    <p class="card-desc">Class aptent taciti sociosqu ad litora torquent per conubia nostra, per inceptos himenaeos.</p>
    <div class="card-art" role="img" aria-label="Glass of white wine" style="background:linear-gradient(#f3f3ef,#e9d774 45%,#c2c2c2)"></div>
    <div class="add-cart">ADD TO CART</div>
  </div>
  <div class="abs card-shadow" style="left:485px"></div>

  <div class="abs card card--sparkling">
    <div class="card-title">SPARKLING</div>
    <div class="card-price">PRICE : <s>$00.00</s><b>$50.00</b></div>
    <p class="card-desc">Class aptent taciti sociosqu ad litora torquent per conubia nostra, per inceptos himenaeos.</p>
    <div class="card-art" role="img" aria-label="Bottle of sparkling wine" style="width:50px;right:28px;background:linear-gradient(#b9a45a,#2e4a2c 30%,#1f3320)"></div>
    <div class="add-cart">ADD TO CART</div>
  </div>
  <div class="abs card-shadow" style="left:810px"></div>

  <section class="abs contact">
    <h2>Contact Us</h2>
    <div class="contact-rule"></div>
    <div class="contact-item" style="left:22px">
      <svg width="20" height="18" viewBox="0 0 20 18"><path d="M10 1L1 9h3v8h5v-5h2v5h5V9h3z" fill="#555"/></svg>
      <span style="font-size:13px">Loreum Ipsum Dollar<br>Loreum Sit Amet.</span>
    </div>
    <div class="contact-item" style="left:276px;top:80px">
      <svg width="18" height="18" viewBox="0 0 18 18"><path d="M3 1l4 1 1 4-2 2c1 2 3 4 5 5l2-2 4 1 1 4-2 1C9 17 1 9 1 3z" fill="#444"/></svg>
      <span>214 480 377</span>
    </div>
    <div class="contact-item" style="left:497px;top:80px">
      <svg width="18" height="18" viewBox="0 0 18 18"><path d="M3 1l4 1 1 4-2 2c1 2 3 4 5 5l2-2 4 1 1 4-2 1C9 17 1 9 1 3z" fill="#444"/></svg>
      <span>Fax : 214 480 378</span>
    </div>
    <div class="contact-item" style="left:739px;top:84px;font-size:13px">
      <svg width="14" height="12" viewBox="0 0 14 12" style="margin-top:3px"><rect x="1" y="1" width="12" height="10" fill="#444"/><path d="M1 1l6 5 6-5" fill="none" stroke="#e3c192" stroke-width="1.2"/></svg>
      <span>info@corklantern.com.au</span>
    </div>
  </section>

  <footer class="abs footer">
    <div class="follow">Follow Us On</div>
    <div class="social" style="left:316px;background:#c5c62d">
      <svg width="38" height="26" viewBox="0 0 38 26"><rect x="2" y="2" width="34" height="22" fill="none" stroke="#fff" stroke-width="2.5"/><path d="M2 2l17 13L36 2" fill="none" stroke="#fff" stroke-width="2.5"/></svg>
    </div>
    <div class="social" style="left:396px;background:#2aa6df">Chirper</div>
    <div class="social" style="left:476px;background:#dc4a35">Circles</div>
    <div class="social" style="left:555px;background:#2a4c8c">Friendbook</div>
    <div class="social" style="left:632px;background:#e5302a">Tubecast</div>
    <div class="social" style="left:708px;background:#176fa5">Linkwork</div>
  </footer>

  <div class="abs copyright">© 2014&nbsp; corklantern.com.au, All Rights Reserved</div>
</div>
</body>
</html>
```